Business Card for Bloom Vitality & Strength

Hi can you please design a business card with my logo and program logo (the new one I just sent) somewhere on it too maybe on the back? Needs to be eye catching and super cool.
Trudy Melcombe, Director
Master Personal Trainer & Nutrition Coach
0472 816 305
Www.bloomvitalitystrength.com.au
Insta (logo) bloom_vitality_strength #bloomyou7x72018

Target Market(s)

30+ women looking to change lifestyle to healthy mind body etc

Industry/Entity Type

Health And Wellness

Contact Information for Business Card

As above

Font styles to use
Sans Serif

Colors

Designer to choose colors to be used in the design.

Requirements
Must have
• Must super cool and edgy with a bit of cuteness

```html
<!DOCTYPE html>
<html lang="en">
<head>
<meta charset="utf-8">
<title>Bloom Vitality &amp; Strength – Business Card</title>
<link rel="stylesheet" href="https://fonts.googleapis.com/css2?family=Lato:wght@400;700;900&display=swap">
<style>
  :root {
    --red: #d90008;
    --charcoal: #343434;
    --charcoal-deep: #262626;
    --paper: #ffffff;
    --paper-cool: #f3f4f6;
    --field: #e6e6e6;
    --ink: #2b2b2b;
    --green: #1fb24a;
    --stage: #e9e7e3;
  }
  * { box-sizing: border-box; margin: 0; padding: 0; }
  html, body { width: 1200px; height: 800px; overflow: hidden; }
  body {
    background: var(--stage);
    font-family: "Lato", Arial, sans-serif;
    color: var(--ink);
    display: flex;
    align-items: center;
    justify-content: center;
    gap: 40px;
  }
  .card {
    position: relative;
    width: 560px;
    height: 320px;
    overflow: hidden;
    box-shadow: 0 6px 20px rgba(0,0,0,.15);
  }

  /* Back */
  .card--back { background: var(--paper); }
  .back__band {
    position: absolute; left: 330px; right: 0; top: 178px; height: 36px;
    background: var(--red); color: #fff;
    font-size: 12px; line-height: 36px; padding-left: 22px; letter-spacing: .3px;
  }
  .program-mark {
    position: absolute; left: 46px; top: 220px;
    display: flex; align-items: center; gap: 8px;
  }
  .program-mark__dot { width: 22px; height: 22px; border-radius: 50%; background: var(--red); }
  .program-mark__name { font-size: 22px; font-weight: 400; color: var(--ink); letter-spacing: 1px; }

  /* Front */
  .card--front { background: var(--paper-cool); }
  .front__rail { position: absolute; left: 0; top: 0; bottom: 0; width: 125px; background: var(--charcoal); }
  .front__rail-inner { position: absolute; left: 62px; top: 0; bottom: 0; width: 63px; background: var(--charcoal-deep); }
  .front__tab {
    position: absolute; left: 0; width: 125px; height: 44px; background: var(--red);
    display: flex; align-items: center; justify-content: flex-end; padding-right: 14px;
  }
  .front__tab svg { width: 20px; height: 20px; fill: #fff; }
  .tab--person { top: 52px; }
  .tab--phone { top: 150px; }
  .tab--web { top: 200px; }

  .identity { position: absolute; left: 148px; top: 60px; }
  .identity__name { font-size: 18px; font-weight: 400; color: var(--ink); }
  .identity__name strong { font-weight: 900; }
  .identity__role { font-size: 11px; }
  .identity__title { font-size: 10px; color: var(--green); margin-top: 3px; }

  .brand-mark {
    position: absolute; left: 340px; top: 104px;
    display: flex; align-items: center; gap: 7px;
  }
  .brand-mark__dot { width: 18px; height: 18px; border-radius: 50%; background: var(--red); flex: none; }
  .brand-mark__name { font-size: 15px; font-weight: 900; color: var(--ink); line-height: 1.1; width: 150px; }

  .field {
    position: absolute; left: 130px; height: 40px; background: var(--field);
    font-size: 12px; color: var(--ink); line-height: 40px; padding-left: 10px;
  }
  .field--phone { top: 152px; width: 175px; }
  .field--web { top: 200px; width: 200px; }

  .front__banner {
    position: absolute; left: 340px; top: 240px; width: 172px; height: 58px;
    background: var(--red); color: #fff; font-size: 15px; font-weight: 700;
    line-height: 58px; padding-left: 18px; letter-spacing: .3px;
  }
  .front__banner-cap { position: absolute; left: 512px; right: 0; top: 240px; height: 58px; background: var(--charcoal); }
</style>
</head>
<body>

  <section class="card card--back" aria-label="Card back">
    <div class="program-mark">
      <span class="program-mark__dot"></span>
      <span class="program-mark__name">BloomYou7x7</span>
    </div>
    <div class="back__band">www.bloomvitalitystrength.com.au</div>
  </section>

  <section class="card card--front" aria-label="Card front">
    <div class="front__rail"><div class="front__rail-inner"></div></div>

    <div class="front__tab tab--person">
      <svg viewBox="0 0 20 20" aria-hidden="true"><circle cx="10" cy="6" r="4.2"/><path d="M2 19c0-5 3.6-7.5 8-7.5s8 2.5 8 7.5z"/></svg>
    </div>
    <div class="front__tab tab--phone">
      <svg viewBox="0 0 20 20" aria-hidden="true"><path d="M2 7c0-2 3-3.5 8-3.5S18 5 18 7v1.5h-4V7H6v1.5H2z"/><path d="M4 10h12l1 8H3z"/><circle cx="10" cy="14" r="2.2" fill="#d90008"/></svg>
    </div>
    <div class="front__tab tab--web">
      <svg viewBox="0 0 20 20" aria-hidden="true"><path d="M2 3h16v11H2zm2 2v7h12V5z"/><path d="M8 14h4v2h3v2H5v-2h3z"/></svg>
    </div>

    <div class="identity">
      <p class="identity__name"><strong>Trudy</strong> Melcombe <span class="identity__role">, Director</span></p>
      <p class="identity__title">Master Personal Trainer &amp; Nutrition Coach</p>
    </div>

    <div class="brand-mark">
      <span class="brand-mark__dot"></span>
      <span class="brand-mark__name">BLOOM VITALITY &amp; STRENGTH</span>
    </div>

    <div class="field field--phone">0472 816 305</div>
    <div class="field field--web">www.bloomvitalitystrength.com.au</div>

    <div class="front__banner">HEALTH &amp; FITNESS</div>
    <div class="front__banner-cap"></div>
  </section>

</body>
</html>
```